Yoga By Marisol Ad for print

I need a print ad designed to go in a brochure for a charity event. I've attached the specs. I need the specs for the 1/2 page ad.
Text for ad:

“E-RYT 200 extensive training with Asana Scholars
Social Media Influencer
Offering group, private and corporate yoga classes
Email: info@yogabymarisol-studio.com
Web: www.yogabymarisol-studio.com
Phone: 480-555-0163
Instagram: @flowofmarisol

Target Market(s)

Yoga practitioners and businesses looking to bring yoga in to their operation.

Font styles to use
Serif
Script

Colors
eda3c7
e34197
eea4c8
f9d9e8
feeeee
000000
1b1b1b
cbcbcb
eaeaea

Requirements
Must have
• One version of my logo, I have provided many to choose from for best aesthetic appeal

```html
<!DOCTYPE html>
<html lang="en">
<head>
<meta charset="utf-8">
<title>Yoga By Marisol – Half Page Ad</title>
<link rel="stylesheet" href="https://fonts.googleapis.com/css2?family=Great+Vibes&family=Lato:ital,wght@0,300;0,400;0,700;1,400;1,700&display=swap">
<style>
  :root {
    --pink: #e34197;
    --pink-soft: #eda3c7;
    --ink: #1b1b1b;
    --white: #ffffff;
    --backdrop: #6f6f6f;
    --sky-top: #4f8fd6;
    --sky-mid: #a9c9ec;
    --cloud: #e8eef6;
    --grass-light: #a8c98a;
    --grass: #6fa24e;
    --rose: #c9736f;
    --skin: #e9bfa6;
  }
  * { box-sizing: border-box; margin: 0; padding: 0; }
  html, body { width: 1200px; height: 1200px; overflow: hidden; }
  body { background: var(--backdrop); position: relative; font-family: "Lato", sans-serif; color: var(--ink); }

  .ad {
    position: absolute; left: 212px; top: 91px;
    width: 777px; height: 1018px; overflow: hidden;
  }
  .ad-photo {
    position: absolute; inset: 0;
    background: linear-gradient(180deg, var(--sky-top) 0%, var(--sky-mid) 30%, var(--cloud) 58%, var(--cloud) 64%, var(--grass-light) 70%, var(--grass) 78%, var(--grass-light) 100%);
  }
  .ad-figure {
    position: absolute; left: 60px; top: 20px; width: 250px; height: 740px;
    border-radius: 120px 120px 40px 40px;
    background: linear-gradient(180deg, var(--skin) 0%, var(--rose) 45%, var(--rose) 100%);
    opacity: 0.55;
  }

  .brand-name {
    position: absolute; right: 57px; top: 305px;
    font-family: "Lato", sans-serif; font-weight: 700; font-size: 38px;
    color: var(--ink); letter-spacing: 1px;
  }

  .headline-lead {
    position: absolute; right: 43px; top: 410px;
    font-family: "Lato", sans-serif; font-weight: 300; font-size: 48px; line-height: 1;
    color: var(--ink); letter-spacing: -0.5px;
  }
  .headline-name {
    position: absolute; right: 60px; top: 448px;
    font-family: "Great Vibes", cursive; font-size: 134px; line-height: 1;
    color: var(--pink);
  }

  .credentials { position: absolute; right: 43px; top: 594px; width: 560px; list-style: none; }
  .credentials li {
    position: relative; text-align: right; padding-right: 46px;
    font-style: italic; font-size: 28px; line-height: 38px; color: var(--ink);
    margin-bottom: 15px;
  }
  .credentials li strong { font-weight: 700; }
  .credentials li::after {
    content: ""; position: absolute; right: 6px; top: 11px;
    width: 17px; height: 17px; border-radius: 50%; background: var(--pink);
  }

  .contact-row { position: absolute; left: 58px; width: 676px; height: 66px; }
  .contact-row.first { top: 836px; }
  .contact-row.second { top: 906px; }
  .contact-dark {
    position: absolute; inset: 0; background: var(--ink); border-radius: 33px;
    display: flex; align-items: center; padding-left: 352px; gap: 10px;
    color: var(--white); font-style: italic; font-size: 20px;
  }
  .contact-pink {
    position: absolute; left: 0; top: 0; bottom: 0; width: 336px;
    background: var(--pink); border-radius: 33px; border: 3px solid var(--white); border-left: none;
    display: flex; align-items: center; padding-left: 14px; gap: 9px;
    color: var(--white); font-style: italic;
  }
  .phone-number { font-weight: 700; font-size: 35px; }
  .web-address { font-size: 17px; letter-spacing: -0.3px; white-space: nowrap; }
  .icon { flex: none; }
  .social-dot { width: 26px; height: 26px; border-radius: 50%; border: 3px solid var(--white); flex: none; }
</style>
</head>
<body>
  <section class="ad">
    <div class="ad-photo" role="img" aria-label="Photo background: blue sky with clouds over a green grassy field"></div>
    <div class="ad-figure" role="img" aria-label="Photo of a yoga instructor in rose leggings holding dancer pose"></div>

    <div class="brand-name">Poised Lotus</div>

    <div class="headline-lead">YOGA BY</div>
    <div class="headline-name">Marisol</div>

    <ul class="credentials">
      <li><strong>E-RYT 200</strong> extensive trained<br>with <strong>Asana Scholars</strong></li>
      <li>Offering <strong>group, private and</strong><br><strong>corporate</strong> yoga classes</li>
      <li><strong>Social media influencer</strong></li>
    </ul>

    <div class="contact-row first">
      <div class="contact-dark">
        <svg class="icon" width="26" height="19" viewBox="0 0 30 22"><rect x="0" y="0" width="30" height="22" rx="2" fill="#fff"/><path d="M1 2 L15 12 L29 2" stroke="#1b1b1b" stroke-width="2.5" fill="none"/></svg>
        <span class="email-address">info@yogabymarisol-studio.com</span>
      </div>
      <div class="contact-pink">
        <svg class="icon" width="24" height="28" viewBox="0 0 26 30"><path d="M6 2 L11 8 L8 12 C10 17 12 20 16 23 L20 20 L25 25 L21 29 C12 27 3 17 2 6 Z" fill="#fff"/></svg>
        <span class="phone-number">480-555-0163</span>
      </div>
    </div>

    <div class="contact-row second">
      <div class="contact-dark">
        <span class="social-dot"></span>
        <span class="social-handle">@flowofmarisol</span>
      </div>
      <div class="contact-pink">
        <svg class="icon" width="28" height="28" viewBox="0 0 32 32" fill="none" stroke="#fff" stroke-width="2.2"><circle cx="16" cy="16" r="14"/><ellipse cx="16" cy="16" rx="6" ry="14"/><path d="M2 16 H30 M5 9 H27 M5 23 H27"/></svg>
        <span class="web-address">www.yogabymarisol-studio.com</span>
      </div>
    </div>
  </section>
</body>
</html>
```